Brand new letterhead, business card, email signature etc.

We are a financial company in London, UK. Our website is www.marlowvane.com. We're wanting a complete remodel of the company colours, letter head, business cards, email signatures, etc. Looking to keep the same font for the company name. I have upload a colour palette that we want to work with. We're looking for company letterhead for outgoing letters/ correspondence, letterhead for internal documentation, email signatures, e-letters. etc. Ultimately we will redesign the entire website also. It is important that our clients get a strong, secure, warm, trustworthy, solid feeling and first impression.
Updates

Designs look the same

Target Market(s)

Institutional investors, (ultra) high net worth individuals

Industry/Entity Type

Finance, Invesments banking.

Font styles to use
Other font styles liked:
• Current font is "Champagne & Limousines"

Requirements
Must have
• Must use the colours provided on the PDF uploaded to the portal. The purple = main colour. The red = accent colour.
Nice to have
• Nice to use same font as now for the company name "Quillmoor". Font is "Champagne & Limousines". Nice to have some reference to the old logo flower, but only subtle.
Should not have
• Do not use the colour red from our website. Use the colours provided on the colour palette PDF that I uploaded in the portal.

```html
<!DOCTYPE html>
<html lang="en">
<head>
<meta charset="utf-8">
<title>Quillmoor Letterhead</title>
<link rel="stylesheet" href="https://fonts.googleapis.com/css2?family=Josefin+Sans:wght@300&display=swap">
<style>
  :root {
    --paper: #ffffff;
    --brand-purple: #4a2760;
    --accent-red: #d63a2a;
    --rule-sand: #dcd6cf;
    --ink: #1f1a24;
    --footer-grey: #6d6a70;
    --petal-light: #f4f2f6;
    --petal-fade: #ffffff;
  }
  * { margin: 0; padding: 0; box-sizing: border-box; }
  html, body { width: 848px; height: 1200px; overflow: hidden; background: var(--paper); }
  .letterhead {
    position: relative;
    width: 848px;
    height: 1200px;
    background: var(--paper);
    font-family: "Josefin Sans", sans-serif;
    font-weight: 300;
    overflow: hidden;
  }
  .brand {
    position: absolute;
    left: 150px;
    top: 56px;
    height: 56px;
    display: flex;
    align-items: center;
    gap: 13px;
  }
  .brand-square {
    width: 56px;
    height: 56px;
    border: 1.5px solid var(--brand-purple);
  }
  .brand-name {
    font-size: 26px;
    letter-spacing: 4px;
    color: var(--brand-purple);
    line-height: 1;
    padding-top: 10px;
    white-space: nowrap;
  }
  .header-rules {
    position: absolute;
    left: 0;
    top: 0;
  }
  .petal-decoration {
    position: absolute;
    left: 370px;
    top: 625px;
    width: 478px;
    height: 470px;
    background: radial-gradient(ellipse at 75% 75%, var(--petal-light) 0%, var(--petal-fade) 70%);
  }
  .footer-rule {
    position: absolute;
    left: 147px;
    top: 1098px;
    width: 553px;
    height: 5px;
    border-radius: 3px;
    background: var(--brand-purple);
  }
  .footer-details {
    position: absolute;
    left: 0;
    top: 1117px;
    width: 848px;
    text-align: center;
    font-size: 9px;
    line-height: 13px;
    color: var(--footer-grey);
  }
</style>
</head>
<body>
<main class="letterhead">
  <header class="brand">
    <div class="brand-square"></div>
    <span class="brand-name">QUILLMOOR</span>
  </header>

  <svg class="header-rules" width="848" height="160" viewBox="0 0 848 160" aria-hidden="true">
    <line x1="148" y1="132" x2="699" y2="132" stroke="var(--brand-purple)" stroke-width="5.5" stroke-linecap="round"/>
    <line x1="147" y1="141" x2="664" y2="141" stroke="var(--rule-sand)" stroke-width="2.5"/>
    <circle cx="672" cy="141" r="1.8" fill="var(--accent-red)"/>
    <circle cx="684" cy="141" r="1.8" fill="var(--accent-red)"/>
    <line x1="147" y1="148" x2="622" y2="148" stroke="var(--ink)" stroke-width="2.5"/>
    <circle cx="626" cy="148" r="2.2" fill="var(--accent-red)"/>
  </svg>

  <div class="petal-decoration" role="img" aria-label="Faint outline of a large flower blossom as background decoration"></div>

  <div class="footer-rule"></div>
  <footer class="footer-details">
    <p>www.marlowvane.com</p>
    <p>Quillmoor (UK) Limited Harrow Court Mayfair</p>
    <p>London W1K 4QT</p>
  </footer>
</main>
</body>
</html>
```